Red Gum Business Card Design

We are a new small business specialising in under ground cable jointing and excavation works in NSW Australia.
Design I'm looking for is incorporating the Australian flag & excavator with out being to cheesy.
Maybe a faded washed out flag to help with overload of colour? & so its not the main focus.
Very open to creative out of the box designs!

Target Market(s)

Building & Construction

Industry/Entity Type

Construction

Contact Information for Business Card

Red Gum Cable Jointing & Excavations
Owen Falkirk

Ph: 0438 605 312
E: owen.falkirk@tallmail.example

Reverse Side
Services we offer:
High Voltage & Low Voltage Cable Jointing
Polymeric & paperlead jointing & terminations
Trenching & Auger Drilling 150 - 600mm
Site preparation / leveling / clearing
Driveway / Footpath / Turf Prep
Rubbish Removal
Tree & Stump removal
Footings & Post holes
Drainage
Service Installs
Gravels & Sands available
Any general Earth moving needs
Reliable Free Quotes
Fully Insured

Font styles to use
Serif
Script

Requirements
Nice to have
• small excavator (See uploaded picture)

```html
<!DOCTYPE html>
<html lang="en">
<head>
<meta charset="utf-8">
<title>Red Gum Business Card Design</title>
<link rel="stylesheet" href="https://fonts.googleapis.com/css2?family=Lobster&family=Tinos&display=swap">
<style>
  :root {
    --plum: #2d1822;
    --plum-text: #3a1f2c;
    --paper: #f1f1f1;
    --ink: #1d1d1d;
    --light-text: #ddd4d8;
    --bg: #e4e2df;
  }
  * { box-sizing: border-box; margin: 0; padding: 0; }
  html, body { width: 1200px; height: 902px; overflow: hidden; background: var(--bg); }
  .card {
    position: absolute; left: 250px; width: 700px; height: 400px; overflow: hidden;
    box-shadow: 0 6px 18px rgba(0,0,0,.18);
  }
  .card--back { top: 40px; background: var(--plum); color: var(--light-text); font-family: "Tinos", serif; }
  .card--front { top: 462px; background: var(--paper); font-family: "Tinos", serif; }

  .torn { position: absolute; left: 0; bottom: 0; width: 700px; height: 100px; }

  /* back */
  .services-title {
    position: absolute; top: 26px; width: 100%; text-align: center;
    font-family: "Lobster", cursive; font-weight: 400; font-size: 32px; color: #fff;
  }
  .services-divider { position: absolute; left: 250px; top: 92px; width: 2px; height: 190px; background: var(--light-text); }
  .services-list { position: absolute; top: 88px; list-style: none; font-size: 18px; line-height: 27px; }
  .services-list--short { right: 468px; text-align: right; }
  .services-list--long { left: 264px; }
  .services-list li { display: flex; align-items: center; gap: 9px; white-space: nowrap; }
  .services-list--short li { justify-content: flex-end; }
  .bullet { width: 10px; height: 10px; border: 2.5px solid var(--light-text); border-radius: 50%; flex: none; }

  /* front */
  .site-photo {
    position: absolute; right: 0; top: 0; width: 300px; height: 330px;
    background: linear-gradient(160deg, #e7e7e7 0%, #bdbdbd 45%, #d77a3c 70%, #6b6b6b 100%);
    -webkit-mask-image: linear-gradient(to right, transparent 0%, #000 35%);
            mask-image: linear-gradient(to right, transparent 0%, #000 35%);
  }
  .business-name {
    position: absolute; left: 40px; top: 56px; white-space: nowrap;
    font-family: "Tinos", serif; font-weight: 400; font-size: 34px; color: var(--plum-text);
  }
  .owner-name { position: absolute; left: 120px; top: 200px; font-size: 34px; color: var(--ink); }
  .contact { position: absolute; left: 350px; top: 130px; padding-left: 16px; border-left: 2px solid var(--ink); font-size: 17px; line-height: 30px; color: var(--ink); }
  .contact li { list-style: none; display: flex; align-items: center; gap: 10px; white-space: nowrap; }
  .contact svg { width: 14px; height: 14px; flex: none; }
</style>
</head>
<body>

<section class="card card--back" aria-label="Card reverse: services">
  <h2 class="services-title">Services we offer:</h2>
  <ul class="services-list services-list--short">
    <li>Drainage<span class="bullet"></span></li>
    <li>Fully Insured<span class="bullet"></span></li>
    <li>Service Installs<span class="bullet"></span></li>
    <li>Rubbish Removal<span class="bullet"></span></li>
    <li>Reliable Free Quotes<span class="bullet"></span></li>
    <li>Tree &amp; Stump removal<span class="bullet"></span></li>
    <li>Footings &amp; Post holes<span class="bullet"></span></li>
  </ul>
  <div class="services-divider"></div>
  <ul class="services-list services-list--long">
    <li><span class="bullet"></span>Gravels &amp; Sands available</li>
    <li><span class="bullet"></span>Driveway / Footpath / Turf Prep</li>
    <li><span class="bullet"></span>Any general Earth moving needs</li>
    <li><span class="bullet"></span>Site preparation / leveling / clearing</li>
    <li><span class="bullet"></span>Trenching &amp; Auger Drilling 150 - 600mm</li>
    <li><span class="bullet"></span>High Voltage &amp; Low Voltage Cable Jointing</li>
    <li><span class="bullet"></span>Polymeric &amp; paperlead jointing &amp; terminations</li>
  </ul>
  <svg class="torn" viewBox="0 0 700 100" preserveAspectRatio="none" aria-hidden="true">
    <polygon fill="#f1f1f1" points="0,42 30,38 55,45 80,36 110,40 140,33 170,41 200,35 235,44 260,38 300,46 330,39 360,47 400,40 430,48 460,41 500,49 530,44 560,52 600,45 630,53 665,47 700,54 700,100 0,100"/>
  </svg>
</section>

<section class="card card--front" aria-label="Card front: contact">
  <div class="site-photo" role="img" aria-label="Photo of a small orange excavator under a cloudy grey sky"></div>
  <h1 class="business-name">Red Gum Cable Jointing &amp; Excavations</h1>
  <ul class="contact">
    <li>
      <svg viewBox="0 0 16 16" aria-hidden="true"><rect x="0.5" y="0.5" width="15" height="15" rx="2" fill="#1d1d1d"/><path d="M5 4c-1 1-1 3 1 5s4 2 5 1l-1.5-1.5-1 .8C7.5 8.8 7.2 8.5 6.7 7.5l.8-1L6 5z" fill="#fff"/></svg>
      0438 605 312
    </li>
    <li>
      <svg viewBox="0 0 16 16" aria-hidden="true"><rect x="0.5" y="0.5" width="15" height="15" rx="2" fill="#1d1d1d"/><rect x="3.5" y="5" width="9" height="6.5" fill="none" stroke="#fff" stroke-width="1.2"/><path d="M3.5 5l4.5 3.5L12.5 5" fill="none" stroke="#fff" stroke-width="1.2"/></svg>
      owen.falkirk@tallmail.example
    </li>
  </ul>
  <p class="owner-name">Owen Falkirk</p>
  <svg class="torn" viewBox="0 0 700 100" preserveAspectRatio="none" aria-hidden="true">
    <polygon fill="#2d1822" points="0,78 40,74 80,80 120,70 160,73 200,62 240,66 280,55 320,58 360,47 400,50 440,38 480,41 520,30 560,33 600,22 640,26 670,16 700,20 700,100 0,100"/>
  </svg>
</section>

</body>
</html>
```